Lanternfold Advisory Business Cards

We need a new layout for our business cards. We have a logo already. But we might be interested in only using the Lanternfold portion of the logo. It has been uploaded.

We would like cards that are not overly busy. Clean. Modern. Perhaps a gray color for one side.

On the back, we would like to have the lanternfold part of the logo and "Take the Leap, we've got you!"

Our business provides medics and safety training for corporate clients. Our website is www.lanternfoldadvisoryllc.example.

Industry/Entity Type

Business

Contact Information for Business Card

We want include name, email address, cell phone, main line number, and website URL on the front. Use the following as an example: Dana Kovrin, dana@lanternfoldadvisoryllc.example, 804.321.7788 (cell), 804.432.919, and www.lanternfoldadvisoryllc.example.

Font styles to use
Serif
Sans Serif

Requirements
Must have
• All required information. Back side logo with "Step forward, we stand beside you!"
Nice to have
• If possible, we would like to consider creating a card in a non-standard shape. Perhaps, the shape of a lanternfold. Just interested in understanding the option.

```html
<!DOCTYPE html>
<html lang="en">
<head>
<meta charset="utf-8">
<title>Lanternfold Advisory Business Cards</title>
<link rel="stylesheet" href="https://fonts.googleapis.com/css2?family=Cinzel:wght@400;600&family=Montserrat:wght@400;700&display=swap">
<style>
  :root {
    --backdrop: #e4e4e4;
    --brand-blue: #1464b4;
    --brand-blue-deep: #0e58a4;
    --card-white: #ffffff;
    --ink-dark: #2a2a2a;
    --ink-light: #ffffff;
  }
  * { box-sizing: border-box; margin: 0; padding: 0; }
  html, body { width: 1200px; height: 800px; overflow: hidden; }
  body {
    background: var(--backdrop);
    font-family: "Montserrat", sans-serif;
    position: relative;
  }
  .card {
    position: absolute;
    width: 540px;
    height: 309px;
    top: 246px;
    overflow: hidden;
    box-shadow: 0 6px 18px rgba(0,0,0,0.12);
  }

  /* Contact side */
  .card--contact {
    left: 30px;
    background: linear-gradient(90deg, var(--brand-blue-deep), var(--brand-blue));
    color: var(--ink-light);
  }
  .contact__mark {
    position: absolute;
    left: 118px;
    top: 96px;
    width: 54px;
    height: 54px;
    border-radius: 50%;
    background: var(--ink-light);
  }
  .contact__rule {
    position: absolute;
    left: 0; top: 0;
  }
  .contact__identity {
    position: absolute;
    left: 206px;
    top: 96px;
  }
  .contact__name { font-weight: 700; font-size: 15px; line-height: 1.2; }
  .contact__role { font-size: 13px; line-height: 1.3; }
  .contact__details {
    position: absolute;
    left: 236px;
    top: 166px;
    font-size: 13px;
    line-height: 1.45;
    list-style: none;
  }

  /* Brand side */
  .card--brand {
    left: 630px;
    background: var(--card-white);
  }
  .brand__mark {
    position: absolute;
    left: 395px;
    top: 52px;
    width: 86px;
    height: 86px;
    border-radius: 50%;
    background: var(--brand-blue);
  }
  .brand__name {
    position: absolute;
    left: 110px;
    top: 136px;
    font-family: "Cinzel", serif;
    font-weight: 600;
    font-size: 22px;
    color: var(--ink-dark);
    letter-spacing: 0.5px;
  }
  .brand__tagline {
    position: absolute;
    left: 132px;
    top: 166px;
    font-family: "Montserrat", sans-serif;
    font-size: 6.5px;
    letter-spacing: 3px;
    text-transform: uppercase;
    color: var(--ink-dark);
  }
  .brand__band {
    position: absolute;
    left: 0;
    top: 196px;
    width: 350px;
    height: 30px;
    background: var(--brand-blue);
    color: var(--ink-light);
    font-family: "Cinzel", serif;
    font-size: 14px;
    line-height: 30px;
    padding-left: 20px;
    letter-spacing: 0.3px;
    white-space: nowrap;
  }
</style>
</head>
<body>

  <section class="card card--contact" aria-label="Business card, contact side">
    <div class="contact__mark"></div>
    <svg class="contact__rule" width="540" height="309" viewBox="0 0 540 309" aria-hidden="true">
      <path d="M168 158 L206 152 L540 152" fill="none" stroke="#ffffff" stroke-width="1.5"/>
    </svg>
    <div class="contact__identity">
      <p class="contact__name">Dana Kovrin</p>
      <p class="contact__role">Designation</p>
    </div>
    <ul class="contact__details">
      <li>804 321 7788 (cell), 804 432 919</li>
      <li>dana@lanternfoldadvisoryllc.example</li>
      <li>www.lanternfoldadvisoryllc.example</li>
    </ul>
  </section>

  <section class="card card--brand" aria-label="Business card, brand side">
    <div class="brand__mark"></div>
    <h1 class="brand__name">Lanternfold Advisory</h1>
    <p class="brand__tagline">The Readiness Partners</p>
    <p class="brand__band">Step forward, we stand beside you!</p>
  </section>

</body>
</html>
```